Brightfold Reach - B2B Demand Generation Website Project

We need a fully functional website for www.brightfoldreach-example.com. We are a B2B Demand Generation company, based in London, working with companies such as QTR, DWN, Vortan, Brelloway, Pelta generating them sales leads for their sales teams. We run this through digital marketing newsletter promotions and have a network of websites. Content syndication, data, demand generation, online marketing. Our logo has just been redone (attached) and we have a holding page already which i would like to use the style / colours. Our logo is bright and vibrant but i dont want the site to be a rainbow. We are expensive, classy, professorial, B2B, intelligent.

Home
About Us
Our Services
Prospero & QA Technology
Intent Data
Testimonials
Contact Us

Target Market(s)

B2B Marketers (QTR, Quorvane, Pelta, DWN, Vista Hub, Harrowby, Tremont Axis, Technology Companies, Data Companies, Marketing Teams, Cloudwick.

Industry/Entity Type

Marketing

Coding

Coded - Design and coding required

Number of Pages Required

5+ page

Font styles to use
Sans Serif

Requirements
Must have
• Home
About Us
Our Services
Prospero & QA Technology
Intent Data
Testimonials
Contact Us

Simple Pages.

Look classy, intelligent, data experts. I like the video homepages were the image moves at the top. Very soft animation.
Nice to have
• Websites i like:

https://www.dwn-example.com/
https://www.pulsegate-example.com/
https://www.lmsitecraft-example.co.uk/

Brightfold Reach - The Demand Generation Company
Should not have
• Pixelvault crap images

```html
<!DOCTYPE html>
<html lang="en">
<head>
<meta charset="utf-8">
<title>Brightfold Reach - The Demand Generation Company</title>
<link href="https://fonts.googleapis.com/css2?family=Poppins:wght@300;400;500;600&display=swap" rel="stylesheet">
<style>
:root{
  --navy:#0d4f91;
  --ink:#1c2234;
  --muted:#7a8194;
  --accent:#d42a3c;
  --deep:#0b0f3a;
  --line:#e6e9f2;
  --white:#ffffff;
}
*{box-sizing:border-box;margin:0;padding:0}
html,body{width:1200px;height:4222px;overflow:hidden;background:var(--white)}
body{font-family:'Poppins',sans-serif;color:var(--ink)}
.page{position:relative;width:1200px;height:4222px;overflow:hidden}
.abs{position:absolute}
.btn{position:absolute;display:flex;align-items:center;justify-content:center;gap:8px;font-size:12px;font-weight:500;border-radius:4px}
.btn-solid{background:var(--navy);color:var(--white)}
.btn-ghost{border:2px solid #d4d9e6;color:var(--ink);background:var(--white)}
.dot-arrow{width:12px;height:12px;border-radius:50%;background:var(--white);display:inline-block}
.btn-ghost .dot-arrow{background:var(--navy)}

/* header */
.brand{display:flex;align-items:center;gap:10px}
.brand-square{width:14px;height:14px;background:var(--navy)}
.brand-name{font-size:21px;font-weight:500;color:var(--navy);line-height:1}
.nav{left:484px;top:54px;display:flex;gap:22px;align-items:center;font-size:11px}
.nav .active{background:var(--navy);color:var(--white);padding:6px 24px;border-radius:14px}
.phone{left:758px;top:18px;font-size:13px;color:var(--navy);display:flex;gap:8px;align-items:center}
.social-top{left:893px;top:16px;display:flex;gap:7px}
.social-top span{width:19px;height:19px;border-radius:50%;border:1px solid #9aa3b8}

/* hero */
.hero-title{left:213px;top:288px;font-size:23px;font-weight:500}
.hero-sub{left:213px;top:336px;width:330px;font-size:10.5px;font-weight:500;line-height:23px}

/* intro */
.intro-lead{left:234px;top:688px;width:330px;font-size:13.5px;line-height:20px}
.intro-para{left:234px;top:810px;width:310px;font-size:10px;line-height:17px;color:#555c6e}
.svc-card{position:absolute;width:125px;height:112px;border-radius:3px;color:var(--white);font-size:10px;text-align:center;display:flex;flex-direction:column;align-items:center;justify-content:flex-end;padding-bottom:14px;gap:8px;box-shadow:0 14px 28px rgba(20,40,90,.18)}
.svc-card .ico{width:28px;height:24px;border:2px solid rgba(255,255,255,.9);border-radius:3px;margin-bottom:6px}

/* mql */
.mql-panel{left:125px;top:1105px;width:465px;height:376px;background:linear-gradient(135deg,#0a4fb6,#1a7cf0)}
.mql-panel h3{position:absolute;left:62px;top:84px;width:330px;font-size:15.5px;font-weight:500;line-height:22px;color:var(--white)}
.mql-panel p{position:absolute;left:62px;top:168px;width:340px;font-size:9.5px;line-height:16px;color:#dbe7ff}
.mql-panel .meet{position:absolute;left:62px;top:250px;width:106px;height:34px;background:var(--white);color:var(--navy);font-size:10.5px;font-weight:500;display:flex;align-items:center;justify-content:center;border-radius:2px}
.tile{position:absolute;color:var(--white);font-size:17.5px;font-weight:500;line-height:28px}
.tile span{position:absolute;left:32px}
.plus-box{left:590px;top:1436px;width:69px;height:64px;background:var(--white);box-shadow:0 10px 30px rgba(20,40,90,.12);display:flex;align-items:center;justify-content:center;color:#8c93a8;font-size:22px;font-weight:300}

/* partners */
.section-icon{left:236px;top:1680px;width:54px;height:54px;border-radius:50%;background:var(--white);box-shadow:0 6px 20px rgba(20,40,90,.12);display:flex;align-items:center;justify-content:center}
.section-icon i{width:14px;height:14px;background:var(--navy)}
.partners-title{left:234px;top:1772px;font-size:17px;font-weight:500}
.partners-para{left:234px;top:1820px;width:290px;font-size:10.5px;line-height:19px;color:#555c6e}
.partner{position:absolute;background:var(--white);box-shadow:0 8px 26px rgba(20,40,90,.12);display:flex;align-items:center;justify-content:center;font-size:14px;font-weight:600;color:var(--navy)}
.trail{position:absolute;border:1px dashed #dfe3ee}

/* quality */
.quality-title{left:672px;top:2286px;width:340px;font-size:15px;font-weight:500;line-height:24px}
.bullets{left:672px;top:2352px;list-style:none;font-size:10px;line-height:21px;color:#7a8194}
.bullets li::before{content:"•";color:var(--navy);margin-right:14px}
.round-arrow{position:absolute;width:30px;height:30px;border-radius:50%;background:var(--navy);display:flex;align-items:center;justify-content:center}

/* qa */
.qa-title{left:279px;top:2636px;font-size:26px;font-weight:500}
.qa-para{left:279px;top:2702px;width:290px;font-size:10.5px;line-height:19px;color:#555c6e}

/* stats */
.stat{position:absolute;color:var(--white)}
.stat h4{font-size:34px;font-weight:300;line-height:38px}
.stat p{font-size:12.5px;margin-top:10px}

/* testimonials */
.quote-title{left:0;width:1200px;top:3526px;text-align:center;font-size:18px;font-weight:500}
.quote-card{left:359px;top:3590px;width:482px;height:275px;background:var(--white);box-shadow:0 10px 40px rgba(20,40,90,.1);text-align:center}
.avatar{position:absolute;left:219px;top:24px;width:44px;height:44px;border-radius:50%;background:#cfd3dc}
.quote-name{position:absolute;top:78px;width:100%;font-size:11px;font-weight:500}
.quote-role{position:absolute;top:96px;width:100%;font-size:9px;color:var(--muted)}
.quote-text{position:absolute;top:132px;left:36px;width:410px;font-size:10px;line-height:18px;color:#555c6e}
.dots{position:absolute;top:226px;width:100%;display:flex;justify-content:center;gap:7px;align-items:center}
.dots span{width:5px;height:5px;border-radius:50%;background:#c2c8d6}
.dots span.on{width:10px;height:10px;background:none;border:1.5px solid var(--navy)}

/* footer */
.footer{left:0;top:3954px;width:1200px;height:268px;background:var(--deep);color:#c6cbe0}
.footer-logo{position:absolute;left:234px;top:65px;width:168px;height:76px;background:var(--white);border-radius:3px;display:flex;align-items:center;justify-content:center}
.footer-logo .brand{gap:7px}
.footer-logo .brand-name{font-size:15px}
.footer-logo .brand-square{width:10px;height:10px}
.copyright{position:absolute;left:239px;top:166px;font-size:9px;color:#9aa1bd}
.fcol{position:absolute;top:80px;font-size:10px}
.fcol h5{font-size:11px;font-weight:500;color:var(--white);margin-bottom:22px}
.fcol li{list-style:none;line-height:23px}
.fsocial{display:flex;gap:10px}
.fsocial span{width:24px;height:24px;border-radius:50%;border:1px solid #3b4270}
.fsocial span.on{background:#1d7be6;border-color:#1d7be6}
</style>
</head>
<body>
<div class="page">

  <!-- header -->
  <div class="abs brand" style="left:234px;top:56px">
    <span class="brand-square"></span>
    <span class="brand-name">Brightfold Reach</span>
  </div>
  <div class="abs phone">
    <svg width="16" height="16" viewBox="0 0 24 24"><path d="M6.6 10.8a15 15 0 0 0 6.6 6.6l2.2-2.2a1 1 0 0 1 1-.25 11.4 11.4 0 0 0 3.6.57 1 1 0 0 1 1 1V20a1 1 0 0 1-1 1A17 17 0 0 1 3 4a1 1 0 0 1 1-1h3.5a1 1 0 0 1 1 1c0 1.25.2 2.45.57 3.6a1 1 0 0 1-.25 1z" fill="none" stroke="currentColor" stroke-width="1.8"/></svg>
    020 7946 0312
  </div>
  <div class="abs social-top"><span></span><span></span><span></span></div>
  <nav class="abs nav">
    <span class="active">Home</span><span>About</span><span>Services</span><span>Technology</span><span>Intent Data</span><span>Testimonials</span><span>Contact</span>
  </nav>

  <!-- hero -->
  <svg class="abs" style="left:0;top:96px" width="1200" height="480" viewBox="0 0 1200 480">
    <defs>
      <linearGradient id="heroPhoto" x1="0" y1="0" x2="1" y2="1">
        <stop offset="0" stop-color="#d9dde4"/><stop offset=".5" stop-color="#b9a48f"/><stop offset="1" stop-color="#6f6a70"/>
      </linearGradient>
    </defs>
    <path d="M1160 0 L1200 40 L1200 330 Q1150 300 1080 320 L1060 250 Z" fill="#2a2060"/>
    <path d="M1200 300 Q1110 330 1080 420 L1200 470 Z" fill="#fdf1e3"/>
    <circle cx="0" cy="305" r="38" fill="none" stroke="#e4e7ef" stroke-width="5"/>
    <circle cx="73" cy="100" r="8" fill="#dbe8fb"/>
    <path d="M246 400 L253 412 L239 412 Z" fill="none" stroke="#b38ad8" stroke-width="2"/>
  </svg>
  <svg class="abs" style="left:541px;top:98px" width="659" height="466" viewBox="0 0 659 466" role="img" aria-label="Photo of a team of colleagues working together around a table with laptops and coffee">
    <path d="M60 0 H659 V320 Q560 520 360 450 Q150 380 60 160 Q20 60 60 0 Z" fill="url(#heroPhoto)"/>
  </svg>
  <h1 class="abs hero-title">B2B Demand Generation</h1>
  <p class="abs hero-sub">Brightfold Reach offers multi-channel demand generation services to publishers and technology</p>
  <div class="btn btn-solid" style="left:213px;top:413px;width:112px;height:32px;border-radius:16px">Explore Now</div>
  <div class="btn btn-ghost" style="left:337px;top:413px;width:112px;height:32px;border-radius:16px">Get A Quote</div>

  <!-- intro -->
  <p class="abs intro-lead">Brightfold Reach offers multi-channel demand generation services to publishers and technology vendors through our network of lead generation websites and native speaking telemarketing agents.</p>
  <p class="abs intro-para">Whether looking for MQL, ABM or BANT campaigns, Brightfold Reach can assist you in delivering your demand generation strategy and generate pipeline for your sales teams and/or channel partners.</p>
  <div class="btn btn-solid" style="left:234px;top:902px;width:116px;height:33px">Learn More <span class="dot-arrow"></span></div>

  <div class="svc-card" style="left:841px;top:664px;background:linear-gradient(135deg,#f7b815,#f5d21a)"><span class="ico" style="border-radius:50%"></span>QA<br>Technology</div>
  <div class="svc-card" style="left:653px;top:790px;background:linear-gradient(135deg,#f0463a,#d91f45)"><span class="ico" style="width:20px"></span>Marketing<br>Qualified Leads</div>
  <div class="svc-card" style="left:741px;top:715px;z-index:2;background:linear-gradient(135deg,#5a3df0,#9b3fe0)"><span class="ico"></span>Account Based<br>Marketing Leads</div>
  <div class="svc-card" style="left:821px;top:833px;z-index:3;background:linear-gradient(135deg,#12b4ee,#1a7fe8)"><span class="ico"></span>Sales Qualified<br>Lead / BANT</div>

  <!-- mql -->
  <div class="abs mql-panel">
    <h3>A Marketing Qualified Lead (MQL) is a prospect that has expressed an interest in what your brand has to offer.</h3>
    <p>An MQL has taken the first steps to becoming a customer and is ready to receive additional contact from your company. From a very general perspective: Marketing Qualified Leads</p>
    <div class="meet">Meet Your Team</div>
  </div>
  <div class="tile" role="img" aria-label="Abstract blue network imagery" style="left:590px;top:1087px;width:286px;height:376px;background:linear-gradient(160deg,#0c3f9e,#2b8fe8 60%,#1557c4)"><span style="top:154px">Marketing<br>Qualified Leads</span></div>
  <div class="tile" role="img" aria-label="Abstract dark network imagery" style="left:876px;top:1087px;width:324px;height:187px;background:linear-gradient(160deg,#1a1a5c,#2a3a9a 70%,#3d7bd8)"><span style="top:60px">Account Based<br>Marketing Leads</span></div>
  <div class="tile" role="img" aria-label="Abstract blue light imagery" style="left:876px;top:1274px;width:324px;height:189px;background:linear-gradient(160deg,#0a1a4a,#1b56b8 60%,#0b1e56)"><span style="top:80px">QA Technology</span></div>
  <div class="abs plus-box">+</div>

  <!-- partners -->
  <svg class="abs" style="left:0;top:1460px" width="1200" height="820" viewBox="0 0 1200 820"><path d="M960 0 L720 300 Q880 560 1200 720" fill="none" stroke="#eef1f7" stroke-width="2"/></svg>
  <div class="trail" style="left:236px;top:1910px;width:398px;height:290px;border-top:none;border-right:none;border-radius:0 0 0 20px"></div>
  <div class="abs section-icon"><i></i></div>
  <h2 class="abs partners-title">Who we work with</h2>
  <p class="abs partners-para">Brightfold Reach offer expert demand generation support, from providing detailed leads of qualified decision-makers, to a comprehensive lead generation and SQL service.</p>
  <div class="btn btn-solid" style="left:234px;top:1931px;width:116px;height:32px">Learn More <span class="dot-arrow"></span></div>
  <div class="btn btn-ghost" style="left:362px;top:1931px;width:104px;height:32px">Support <span class="dot-arrow"></span></div>

  <div class="partner" style="left:923px;top:1676px;width:108px;height:78px">Tallyfern</div>
  <div class="partner" style="left:739px;top:1718px;width:120px;height:89px">Pelta</div>
  <div class="partner" style="left:570px;top:1776px;width:140px;height:75px">DWN</div>
  <div class="partner" style="left:1044px;top:1748px;width:95px;height:65px">Norvique</div>
  <div class="partner" style="left:851px;top:1818px;width:115px;height:85px">Cloudmere</div>
  <div class="partner" style="left:989px;top:1857px;width:137px;height:74px">Ardentis</div>
  <div class="partner" style="left:695px;top:1872px;width:130px;height:118px;font-size:22px">QTR</div>
  <div class="partner" style="left:895px;top:1943px;width:105px;height:90px">Kestrel</div>
  <div class="partner" style="left:797px;top:2054px;width:139px;height:72px">Pavona</div>

  <!-- quality -->
  <div class="trail" style="left:236px;top:2200px;width:398px;height:350px;border-radius:20px"></div>
  <div class="abs" role="img" aria-label="Illustration of a team building a lead dashboard with boxes and charts" style="left:246px;top:2262px;width:344px;height:254px;background:linear-gradient(135deg,#e9e6fb,#b7b0f0 55%,#f5b44a);border-radius:6px;opacity:.9"></div>
  <h3 class="abs quality-title">Brightfold Reach can deliver high quality sales leads from any country in the world</h3>
  <ul class="abs bullets">
    <li>Breakdown by geography, job title, role and responsibility</li>
    <li>Targeting through previous research and buying intention</li>
    <li>Email dispatch to selected individuals</li>
    <li>Extensive telemarketing options</li>
  </ul>
  <div class="round-arrow" style="left:672px;top:2448px"><svg width="12" height="12" viewBox="0 0 12 12"><path d="M2 6h8M7 3l3 3-3 3" stroke="#fff" stroke-width="1.5" fill="none"/></svg></div>

  <!-- qa -->
  <div class="trail" style="left:236px;top:2600px;width:398px;height:360px;border-right:none;border-bottom:none;border-top:none"></div>
  <h2 class="abs qa-title">QA Technology:</h2>
  <p class="abs qa-para">Prospero is a proprietary lead verification platform from Brightfold Reach that aims to sift out invalid leads with questionable or erroneous data. The platform is designed to equip sales teams with accurate, high-quality records in order to improve lead generation, accelerate pipeline and increase revenue.</p>
  <div class="btn btn-solid" style="left:279px;top:2849px;width:86px;height:30px;font-size:9px">Learn More</div>
  <div class="abs" role="img" aria-label="Illustration of colleagues collaborating around a desk with laptops" style="left:607px;top:2606px;width:409px;height:230px;background:linear-gradient(135deg,#eef0f8,#c9cde6 50%,#8fb77a);border-radius:6px;opacity:.85"></div>

  <!-- stats -->
  <svg class="abs" style="left:0;top:3000px" width="1200" height="440" viewBox="0 0 1200 440" role="img" aria-label="Blue abstract network band">
    <defs><linearGradient id="statsBg" x1="0" y1="0" x2="1" y2="1"><stop offset="0" stop-color="#1466c8"/><stop offset=".55" stop-color="#0f4fa8"/><stop offset="1" stop-color="#2f86e0"/></linearGradient></defs>
    <path d="M0 20 Q300 -5 600 15 T1200 0 V440 H0 Z" fill="url(#statsBg)"/>
    <path d="M870 0 Q900 90 990 110 L1015 145 L1030 105 Q1140 60 1150 0 Z" fill="#fff"/>
  </svg>
  <div class="stat" style="left:234px;top:3095px"><h4>Downloads<br>Per Month</h4><p>Ticker to 70,000+</p></div>
  <div class="stat" style="left:234px;top:3242px"><h4>Leads Delivered<br>Per Month</h4><p>Ticker 25,000+</p></div>
  <div class="stat" style="left:556px;top:3160px"><h4>Countries We<br>Can Reach</h4><p>Ticker to 50+</p></div>

  <!-- testimonials -->
  <h2 class="abs quote-title">We've heard things like</h2>
  <div class="round-arrow" style="left:234px;top:3708px;background:none;border:1px solid #e0e4ee"><svg width="12" height="12" viewBox="0 0 12 12"><path d="M10 6H2M5 3 2 6l3 3" stroke="#7a8194" stroke-width="1.3" fill="none"/></svg></div>
  <div class="round-arrow" style="left:934px;top:3708px;background:#1d7be6"><svg width="12" height="12" viewBox="0 0 12 12"><path d="M2 6h8M7 3l3 3-3 3" stroke="#fff" stroke-width="1.5" fill="none"/></svg></div>
  <div class="abs quote-card">
    <div class="avatar" role="img" aria-label="Client portrait"></div>
    <div class="quote-name">Tobin Marlowe</div>
    <div class="quote-role">Project Manager</div>
    <p class="quote-text">What a load of rubbish bits and bobs pear shaped owt to do with me bubble and squeak jolly good morish tinkety tonk old fruit, car boot my good sir buggered plastered cheeky David, haggle young delinquent say so I said bite your arm off easy peasy. Skive off it's all gone to pot buggered.</p>
    <div class="dots"><span></span><span></span><span></span><span class="on"></span></div>
  </div>

  <!-- footer -->
  <footer class="abs footer">
    <div class="footer-logo"><div class="brand"><span class="brand-square"></span><span class="brand-name">Brightfold Reach</span></div></div>
    <div class="copyright">Copyright © 2020 Brightfold Reach</div>
    <div class="fcol" style="left:484px"><h5>Quick Link</h5><ul><li>Home</li><li>About</li><li>Services</li><li>Support</li></ul></div>
    <div class="fcol" style="left:670px"><h5>Quick Link</h5><ul><li>Technology</li><li>Intent Data</li><li>Testmonials</li><li>Contact Us</li></ul></div>
    <div class="fcol" style="left:859px"><h5>Follow Us</h5><div class="fsocial"><span></span><span class="on"></span><span></span><span></span></div></div>
  </footer>
</div>
</body>
</html>
```